Business card like design

Hello we need a business card like design, not with personal info. But with info from our shop, like address, phone, street, email, facebook .....
This cards we put in the box when we send out the orders......
Target Market(s)
We sell cheap sunglasses, our customers are mainly young adults, that like going to parties
Industry/Entity Type
Business

```html
<!DOCTYPE html>
<html lang="nl">
<head>
<meta charset="utf-8">
<title>brightshades.nl – kaartje</title>
<link href="https://fonts.googleapis.com/css2?family=Questrial&display=swap" rel="stylesheet">
<style>
  :root {
    --bg: #d9d9d9;
    --card: #ffffff;
    --ink: #231f20;
    --orange: #f7941d;
    --sand: #f6d3a0;
    --ghost-light: #efefef;
    --ghost-dark: #3b3738;
  }
  * { margin: 0; padding: 0; box-sizing: border-box; }
  html, body { width: 1200px; height: 793px; overflow: hidden; background: var(--bg); }
  body { position: relative; font-family: "Questrial", "Century Gothic", sans-serif; }

  .card {
    position: absolute; top: 236px; width: 560px; height: 320px;
    background: var(--card); overflow: hidden;
    box-shadow: 0 2px 8px rgba(0,0,0,.18);
  }
  .card--front { left: 27px; }
  .card--back { left: 613px; }
  .card__shapes { position: absolute; inset: 0; }

  .brand {
    position: absolute; display: flex; align-items: center; gap: 12px;
    color: var(--ink); font-size: 38px; letter-spacing: .5px; white-space: nowrap;
  }
  .brand__dot { width: 30px; height: 30px; border-radius: 50%; background: var(--orange); flex: none; }
  .card--front .brand { left: 50%; top: 140px; transform: translateX(-50%); }
  .card--back .brand { left: 175px; top: 140px; transform: translateX(-50%); font-size: 32px; }

  .ghost { position: absolute; white-space: nowrap; pointer-events: none; }
  .ghost--front { color: var(--ghost-light); font-size: 74px; left: 40px; bottom: -14px; letter-spacing: 1px; }
  .ghost--back {
    color: var(--ghost-dark); font-size: 34px; right: -128px; top: 150px;
    transform: rotate(90deg); transform-origin: center; letter-spacing: 1px;
  }

  .contact {
    position: absolute; right: 22px; top: 78px; list-style: none;
    display: flex; flex-direction: column; gap: 14px;
    color: var(--orange); font-size: 12.5px; text-align: right; line-height: 1.45;
  }
  .contact__item { display: flex; align-items: center; justify-content: flex-end; gap: 8px; }
  .contact__icon {
    width: 20px; height: 20px; border-radius: 50%; background: var(--sand);
    display: flex; align-items: center; justify-content: center; flex: none;
  }
  .contact__icon svg { width: 12px; height: 12px; fill: var(--ink); }
  .contact__item--social { margin-top: -2px; }
</style>
</head>
<body>

<section class="card card--front" aria-label="Voorkant">
  <svg class="card__shapes" viewBox="0 0 560 320" aria-hidden="true">
    <polygon points="0,0 560,0 560,42 0,22" fill="var(--ink)"/>
    <polygon points="0,22 72,26 0,56" fill="var(--orange)"/>
  </svg>
  <div class="ghost ghost--front">brightshades.nl</div>
  <div class="brand"><span class="brand__dot"></span>brightshades.nl</div>
</section>

<section class="card card--back" aria-label="Achterkant">
  <svg class="card__shapes" viewBox="0 0 560 320" aria-hidden="true">
    <rect x="352" y="0" width="208" height="320" fill="var(--ink)"/>
    <polygon points="288,0 352,0 352,78" fill="var(--orange)"/>
  </svg>
  <div class="ghost ghost--back">brightshades.nl</div>
  <div class="brand"><span class="brand__dot"></span>brightshades.nl</div>

  <ul class="contact">
    <li class="contact__item">
      <span>Havenkade 12 4811 AB<br>Breda Nederland</span>
      <span class="contact__icon"><svg viewBox="0 0 12 12"><path d="M6 0.5a3.8 3.8 0 0 0-3.8 3.8C2.2 7.3 6 11.5 6 11.5s3.8-4.2 3.8-7.2A3.8 3.8 0 0 0 6 .5zm0 5.3a1.5 1.5 0 1 1 0-3 1.5 1.5 0 0 1 0 3z"/></svg></span>
    </li>
    <li class="contact__item">
      <span>003176 555 01 23</span>
      <span class="contact__icon"><svg viewBox="0 0 12 12"><path d="M1 4.5C1 3 3 2 6 2s5 1 5 2.5V5.5H8.5V4.3C7.7 4 6.9 3.9 6 3.9S4.3 4 3.5 4.3v1.2H1zM3 6h6l1.5 4.5h-9zM6 7.2a1.3 1.3 0 1 0 0 2.6 1.3 1.3 0 0 0 0-2.6z"/></svg></span>
    </li>
    <li class="contact__item">
      <span>info@BrightShades.nl</span>
      <span class="contact__icon"><svg viewBox="0 0 12 12"><path d="M1 2.5h10v7H1zM1.8 3.3 6 6.6l4.2-3.3z" fill-rule="evenodd"/></svg></span>
    </li>
    <li class="contact__item contact__item--social">
      <span>social.brightshades.nl</span>
      <span class="contact__icon"></span>
    </li>
  </ul>
</section>

</body>
</html>
```